Design a box for EV Charging Cables - Electric Cars

https://files.plomtrex.example/doc/7qRwLm2ZxNa9/view

We are looking to design a box to package our EV charging cables. This box needs to be 40cm x 40cm x 11cm.

It needs to include:
- Our logo
- Images of our products
- Accreditations

My websites are:
https://voltharbor.co.uk/
https://www.plugmerrow.co.uk/
https://www.zandrel-amp.co.uk/

Logo:
https://pixdrop.example/Kq8Tz2L
https://pixdrop.example/Rw4Hn9B
https://pixdrop.example/Jd7Pv3X
https://pixdrop.example/Ny6Qb5G

Rather than having a list of products. I would like to have tick boxes:
1st tick box: Connector Type From: (Type 2, 3 Pin),
2nd tick box: Connector Type To: (Type 1, Type 2),
3rd tick box: Amp/Charge Speed (13amp/16amp/32amp/32amp - 3 Phase)
4th tick box: Length (5m/10m/15m)

Target Market(s)

People who own electric cars

Industry/Entity Type

Automotive

Colors

Designer to choose colors to be used in the design.

Requirements
Must have
• Our colours, logo, list of products we sell
Nice to have
• Rather than having a list of products. I would like to have tick boxes: 1st tick box should be: Connector Type From: (Type 2, 3 Pin), Connector Type To: (Type 1, Type 2), Third: Amp/Charge Speed (13amp/16amp/32amp/32amp - 3 Phase) Third: Length (5m/10m/15m)
Should not have
• Transparent Section

```html
<!DOCTYPE html>
<html lang="en">
<head>
<meta charset="utf-8">
<title>Voltharbor – EV Charging Cables Box Front</title>
<link rel="stylesheet" href="https://fonts.googleapis.com/css2?family=Exo+2:ital,wght@0,800;1,800&display=swap">
<style>
  :root {
    --panel-black: #0d0e0d;
    --panel-black-soft: #1b1d1b;
    --brand-green: #5fbf2a;
    --brand-lime: #a9d43a;
    --deep-green: #1f6e1c;
    --silver-light: #e9ecef;
    --silver-mid: #b9bec4;
    --silver-dark: #8d9299;
    --cable-green: #7ee860;
  }
  * { margin: 0; padding: 0; box-sizing: border-box; }
  html, body {
    width: 1200px;
    height: 1200px;
    overflow: hidden;
    background: var(--panel-black);
  }
  .box-front {
    position: relative;
    width: 1200px;
    height: 1200px;
    background: radial-gradient(ellipse at 70% 30%, var(--panel-black-soft) 0%, var(--panel-black) 70%);
    overflow: hidden;
    font-family: "Exo 2", sans-serif;
  }
  .pattern-fan {
    position: absolute;
    left: 680px;
    top: 30px;
    width: 480px;
    height: 880px;
    clip-path: polygon(18% 0, 100% 0, 92% 100%, 0 85%);
    background: linear-gradient(180deg, rgba(31,110,28,0.05) 0%, rgba(31,110,28,0.28) 55%, rgba(31,110,28,0.4) 100%);
  }
  .pattern-sweep {
    position: absolute;
    left: 0;
    top: 560px;
    width: 1200px;
    height: 440px;
    clip-path: polygon(0 0, 100% 75%, 100% 100%, 0 25%);
    background: linear-gradient(90deg, rgba(95,191,42,0.55) 0%, rgba(95,191,42,0.35) 60%, rgba(95,191,42,0.2) 100%);
  }
  .product-title {
    position: absolute;
    left: 600px;
    top: 90px;
    font-style: italic;
    font-weight: 800;
    font-size: 80px;
    line-height: 1.05;
    letter-spacing: 2px;
    text-transform: uppercase;
    background: linear-gradient(180deg, var(--silver-light) 0%, var(--silver-mid) 60%, var(--silver-dark) 100%);
    -webkit-background-clip: text;
    background-clip: text;
    color: transparent;
  }
  .brand-mark {
    position: absolute;
    left: 60px;
    top: 390px;
    display: flex;
    align-items: center;
    gap: 20px;
  }
  .brand-dot {
    width: 56px;
    height: 56px;
    border-radius: 50%;
    background: var(--brand-green);
  }
  .brand-name {
    font-weight: 800;
    font-size: 84px;
    letter-spacing: 2px;
    color: var(--brand-green);
    line-height: 1;
  }
  .product-photo {
    position: absolute;
    left: 0;
    top: 720px;
    width: 1010px;
    height: 480px;
    clip-path: polygon(0 0, 100% 26%, 100% 100%, 0 100%);
    background:
      radial-gradient(ellipse 55% 45% at 45% 55%, rgba(20,22,20,0.95) 0%, rgba(20,22,20,0.85) 45%, rgba(20,22,20,0) 72%),
      radial-gradient(ellipse 20% 12% at 30% 82%, rgba(126,232,96,0.55) 0%, rgba(126,232,96,0) 100%),
      linear-gradient(110deg, var(--silver-light) 0%, var(--silver-mid) 45%, var(--silver-dark) 75%, var(--silver-light) 100%);
  }
</style>
</head>
<body>
  <main class="box-front">
    <div class="pattern-fan" role="img" aria-label="Decorative fan of thin green lines"></div>
    <div class="pattern-sweep" role="img" aria-label="Decorative diagonal green line sweep"></div>

    <h1 class="product-title">EV Charging<br>Cables</h1>

    <div class="brand-mark">
      <span class="brand-dot"></span>
      <span class="brand-name">VOLTHARBOR</span>
    </div>

    <div class="product-photo" role="img" aria-label="Product photo: coiled black EV charging cable with green-trimmed connectors on a silver background"></div>
  </main>
</body>
</html>
```